Tendril Harbor

Our product is a subscription-based website for doctors and medical practices. It allows contract-based doctors (locums) to book jobs with medical practices and to organise their own finances (invoicing, pension, etc). Also, it allows medical practices to post jobs, and book locums.

We need a website design that looks clean and professional. It should look easy-to-use and friendly, which will encourage users to sign up as they'll hopefully think using the system will also be simple and friendly.

As well as the homepage, we need a design for the logged-in view. This is very different to the website but equally important. It needs to be very functional. Much more like an application and less like a website.

PLEASE SUBMIT BOTH WEBSITE HOMEPAGE DESIGN AND APPLICATION DASHBOARD DESIGN.

The application is built and we already have a user interface (linked below) so we're not looking for a designer to decide what is on these pages - we already have that. We're ONLY asking for visual design. Please just make the content we have look good. You may move parts of the content around a small amount but the functionality is very much signed off now so it's only visual styling that we need addressed.

Please base the branding around the current logo, which can't be changed. You can get the logo as an EPS here : http://clients.brassowl.co.uk/tendrilharbor/design/logo-green.eps

Here is a link to the current design for the website, and for the application dashboard:
http://clients.brassowl.co.uk/tendrilharbor/design/

Also, here is a video we've had made which might help you with the brand:
http://quivlo.com/71825364
Updates

Just in case it isn't clear, the video (linked in the main brief) is an essential part of the website homepage.

Reason: We need to spend some time looking over these designs and might ask for a few amendments to one or two in the next few days. Thanks.

Target Market(s)

Doctors and medical practices

Industry/Entity Type

Medical

Requirements
Must have
• It must have all the features that are in the linked designs - homepage and dashboard.

```html
<!DOCTYPE html>
<html lang="en">
<head>
<meta charset="utf-8">
<title>Tendril Harbor – Dashboard</title>
<link href="https://fonts.googleapis.com/css2?family=Open+Sans:wght@400;600;700&display=swap" rel="stylesheet">
<style>
:root{
  --sky:#e6f1f8;
  --bar:#1a88bf;
  --bar-dark:#0f6c9e;
  --navy:#0b4f78;
  --green:#6cae1d;
  --green-dark:#4f8a0f;
  --orange:#f08a1e;
  --orange-dark:#d9700c;
  --text:#4a4a4a;
  --muted:#777;
  --link:#2a9fd6;
  --panel-head:#e6eafb;
  --line:#d9dde3;
  --busy:#d7191c;
  --partial:#f49b26;
  --free:#5cb432;
  --empty:#e2e2e2;
  --logo-blue:#1b7db3;
}
*{box-sizing:border-box;margin:0;padding:0}
html,body{width:1200px;height:1184px;overflow:hidden}
body{font-family:"Open Sans",Arial,sans-serif;color:var(--text);font-size:12px;
  background:linear-gradient(180deg,#cfe4f2 0,#f3f8fc 260px,#eef4f8 100%);position:relative}
.topbar{position:absolute;left:0;top:0;width:1200px;height:40px;background:linear-gradient(#1f95cc,var(--bar-dark));}
.topbar a{position:absolute;top:11px;color:#fff;font-size:14px;text-decoration:none;letter-spacing:.3px}
.topbar .sep{position:absolute;top:12px;width:1px;height:16px;background:rgba(255,255,255,.35)}
.user-btn{position:absolute;left:965px;top:9px;width:193px;height:32px;background:linear-gradient(#7cc12a,var(--green-dark));border-radius:3px 3px 0 0;color:#fff;font-size:14px;font-weight:600;display:flex;align-items:center}
.user-btn span{flex:1;text-align:center}
.user-btn i{width:28px;height:100%;border-left:1px solid rgba(255,255,255,.35);display:flex;align-items:center;justify-content:center}
.brand{position:absolute;left:76px;top:58px;display:flex;align-items:center;gap:14px}
.brand-dot{width:60px;height:60px;border-radius:50%;background:var(--logo-blue)}
.brand-name{font-size:30px;font-weight:700;color:var(--logo-blue);line-height:1}
.cta{position:absolute;left:967px;top:70px;width:191px;height:37px;background:linear-gradient(#f7a040,var(--orange-dark));color:#fff;font-size:14px;text-align:center;line-height:37px;border-radius:2px;letter-spacing:.3px}
.tabs{position:absolute;left:74px;top:153px;display:flex}
.tab{width:196px;height:38px;background:linear-gradient(#fafafa,#e3e5e8);border-radius:6px 6px 0 0;margin-right:0;text-align:center;line-height:40px;font-size:14px;font-weight:600;color:#8fb3cc;letter-spacing:.5px;border:1px solid #e0e3e6;border-bottom:none}
.tab.active{background:#fff;color:#6b6b6b;height:39px;width:201px}
.main{position:absolute;left:58px;top:191px;width:1100px;height:921px;background:#fff;border-radius:0 4px 6px 6px;box-shadow:0 1px 4px rgba(0,0,0,.12)}
.notice{position:absolute;left:41px;top:217px;width:773px;height:35px;display:flex;background:var(--bar)}
.notice .label{width:185px;background:var(--navy);color:#fff;font-size:15px;line-height:35px;padding-left:30px;letter-spacing:.3px}
.notice .msg{color:#fff;font-size:14px;line-height:35px;padding-left:12px;display:flex;align-items:center;gap:10px}
.notice .fold{position:absolute;left:0;top:35px;width:0;height:0;border-top:14px solid #083a59;border-left:14px solid transparent}
.panel{position:absolute;border:1px solid var(--line);background:#fafbfc}
.panel-head{height:44px;background:linear-gradient(#fff,var(--panel-head));border-bottom:1px solid var(--line);font-size:14px;color:#6b6b6b;line-height:44px;padding-left:20px;letter-spacing:.3px}
.jobs{left:75px;top:276px;width:739px;height:443px}
.jobs .panel-head{height:45px}
.map{position:absolute;left:6px;top:50px;width:727px;height:296px;background:linear-gradient(135deg,#e8e1cf,#d9dfc7 45%,#e5ddc8);}
.job-table{position:absolute;left:4px;top:354px;width:729px}
.job-row{display:flex;height:39px;border:1px solid var(--line);border-top:none;background:linear-gradient(#fff,#eef0f2)}
.job-row:first-child{border-top:1px solid var(--line)}
.job-row div{border-right:1px solid var(--line);display:flex;align-items:center;font-size:12px}
.job-row div:last-child{border-right:none}
.c-name{width:193px;padding-left:10px;gap:12px}
.c-jobs{width:185px;justify-content:center}
.c-dist{width:138px;justify-content:center}
.c-link{flex:1;justify-content:center;color:var(--link)}
.diary{left:75px;top:730px;width:456px;height:210px;background:#fff}
.diary-body{display:flex;height:165px}
.legend{width:150px;padding:14px 0 0 15px;position:relative}
.legend li{list-style:none;display:flex;align-items:center;gap:8px;font-size:10px;color:#666;margin-bottom:10px}
.legend b{width:18px;height:13px;border-radius:2px;display:block}
.legend a{position:absolute;left:15px;bottom:8px;font-size:10px;color:var(--link)}
.cal{flex:1;border-left:1px solid var(--line)}
.cal-title{height:32px;line-height:32px;text-align:center;font-size:12px;background:#f6f7f8;border-bottom:1px solid var(--line)}
.cal-days,.cal-grid{display:grid;grid-template-columns:repeat(7,1fr)}
.cal-days span{font-size:10px;color:#888;text-align:center;height:26px;line-height:26px;background:#f2f3f4}
.cal-grid span{height:21px;line-height:21px;text-align:center;color:#fff;font-size:10px;font-weight:600;border:1px solid #fff}
.b{background:var(--busy)}.p{background:var(--partial)}.f{background:var(--free)}.e{background:var(--empty)}
.side{left:837px;width:300px;background:#fff}
.side .panel-head{height:37px;line-height:37px;padding-left:15px}
.job-card{padding:10px 15px 0;height:92px;display:flex;justify-content:space-between;background:#fff}
.job-card h4{font-size:13px;font-weight:600;color:#333;margin-bottom:2px}
.job-card p{font-size:12px;color:#777;line-height:17px}
.job-card .when{color:var(--link);font-size:11px;width:140px;line-height:15px}
.job-foot{background:var(--panel-head);padding:8px 15px;font-size:11px;color:#666;line-height:18px;height:53px}
.job-foot em{font-style:normal;color:var(--green)}
.stat{display:flex;justify-content:space-between;align-items:center;height:32px;padding:0 15px;border-top:1px solid var(--line);font-size:11px;background:linear-gradient(#fff,#f4f5f6)}
.stat b{color:var(--link);font-weight:600}
.stat.total{background:#e7eeee}
.fin-tabs{display:flex;height:30px;border-bottom:1px solid var(--line)}
.fin-tabs span{flex:1;display:flex;align-items:center;gap:8px;padding-left:18px;font-size:11px;background:linear-gradient(#fff,#eef0f2)}
.fin-tabs span+span{border-left:1px solid var(--line)}
.radio{width:9px;height:9px;border-radius:50%;border:1px solid #aaa;background:#fff}
.radio.on{background:var(--bar);border-color:var(--bar)}
.footer{position:absolute;top:1141px;left:58px;width:1100px;display:flex;font-size:11px;color:#555;letter-spacing:.2px}
.footer .links{margin-left:auto;display:flex;gap:20px}
</style>
</head>
<body>
<header class="topbar">
  <a style="left:756px">SETTINGS</a>
  <span class="sep" style="left:849px"></span>
  <a style="left:877px">REFERAL</a>
  <div class="user-btn"><span>Mrs Helena Marsh</span><i><svg width="8" height="10"><path d="M0 0L8 5 0 10z" fill="#fff"/></svg></i></div>
</header>

<div class="brand"><span class="brand-dot"></span><span class="brand-name">Tendril Harbor</span></div>
<div class="cta">GET STARTED</div>

<nav class="tabs">
  <div class="tab active">DASHBOARD</div>
  <div class="tab">PROFILE</div>
  <div class="tab">MY JOBS</div>
  <div class="tab">MY FINANCES</div>
  <div class="tab">MY NETWORK</div>
</nav>

<main class="main"></main>

<div class="notice">
  <div class="label">NOTIFICATIONS</div>
  <div class="msg"><svg width="16" height="16"><circle cx="8" cy="8" r="8" fill="#e0201c"/><rect x="7" y="3.5" width="2" height="6" fill="#fff"/><rect x="7" y="11" width="2" height="2" fill="#fff"/></svg>Mill Lane Surgery has posted a new job.</div>
  <span class="fold"></span>
</div>

<section class="panel jobs">
  <div class="panel-head">Jobs within 20 miles</div>
  <div class="map" role="img" aria-label="Street map of east London showing nearby surgeries with job markers"></div>
  <div class="job-table">
    <div class="job-row">
      <div class="c-name"><svg width="14" height="20"><path d="M7 0a7 7 0 0 1 7 7c0 5-7 13-7 13S0 12 0 7a7 7 0 0 1 7-7z" fill="#f26b5b"/><text x="7" y="10" font-size="8" fill="#fff" text-anchor="middle" font-family="Open Sans,sans-serif">A</text></svg>Willowmere Surgery</div>
      <div class="c-jobs">14 Jobs Available</div>
      <div class="c-dist">0.8 miles</div>
      <div class="c-link">View more details</div>
    </div>
    <div class="job-row">
      <div class="c-name"><svg width="14" height="20"><path d="M7 0a7 7 0 0 1 7 7c0 5-7 13-7 13S0 12 0 7a7 7 0 0 1 7-7z" fill="#f26b5b"/><text x="7" y="10" font-size="8" fill="#fff" text-anchor="middle" font-family="Open Sans,sans-serif">B</text></svg>Mill Lane Surgery</div>
      <div class="c-jobs">0 Jobs Available</div>
      <div class="c-dist">2.73 miles</div>
      <div class="c-link">View more details</div>
    </div>
  </div>
</section>

<section class="panel diary">
  <div class="panel-head">MY DIARY</div>
  <div class="diary-body">
    <ul class="legend">
      <li><b class="b"></b>Busy</li>
      <li><b class="p"></b>Partially available</li>
      <li><b class="f"></b>Available</li>
      <a>See all appointments</a>
    </ul>
    <div class="cal">
      <div class="cal-title">January 2013</div>
      <div class="cal-days"><span>Sun</span><span>Mon</span><span>Tue</span><span>Wed</span><span>Thu</span><span>Fri</span><span>Sat</span></div>
      <div class="cal-grid">
        <span class="e"></span><span class="b">1</span><span class="f">2</span><span class="p">3</span><span class="p">4</span><span class="p">5</span><span class="f">6</span>
        <span class="b">7</span><span class="b">8</span><span class="f">9</span><span class="f">10</span><span class="f">11</span><span class="f">12</span><span class="f">13</span>
        <span class="f">14</span><span class="f">15</span><span class="f">16</span><span class="b">17</span><span class="b">18</span><span class="f">19</span><span class="f">20</span>
        <span class="f">21</span><span class="f">22</span><span class="f">23</span><span class="p">24</span><span class="p">25</span><span class="f">26</span><span class="f">27</span>
        <span class="b">28</span><span class="b">29</span><span class="f">30</span><span class="f">31</span><span class="e"></span><span class="e"></span><span class="e"></span>
      </div>
    </div>
  </div>
</section>

<section class="panel side" style="top:216px;height:194px">
  <div class="panel-head">CURRENT OR NEXT JOB</div>
  <div class="job-card">
    <div><h4>Ashgrove Surgery</h4><p>42 Elm Parade,<br>London<br>N7 2QD</p></div>
    <div class="when">17 Jan 2012 - 24 Jan 2013<br>(09.30 - 16.00)</div>
  </div>
  <div class="job-foot">* Earnings from this employer: <em>£23,887</em><br>* This surgery has <em>8</em> unfilled jobs</div>
</section>

<section class="panel side" style="top:425px;height:188px">
  <div class="panel-head">FOLLOWING</div>
  <div class="job-card">
    <div><h4>Dr Renfrew Surgery</h4><p>42 Elm Parade,<br>London<br>N7 2QD</p></div>
    <div class="when">23 Jan 2012 (09.30 - 15.30)</div>
  </div>
  <div class="job-foot" style="height:50px">* Earnings from this employer: <em>£6,523</em><br>* This surgery has no unfilled jobs</div>
</section>

<section class="panel side" style="top:633px;height:193px">
  <div class="panel-head">MY JOBS</div>
  <div class="stat"><span>Jobs Booked</span><b>17</b></div>
  <div class="stat"><span>Jobs Requiring Confirmation</span><b>0</b></div>
  <div class="stat"><span>Pending Applications</span><b>2</b></div>
  <div class="stat"><span>Jobs Invited</span><b>1</b></div>
  <div class="stat"><span>My Network</span><b>9</b></div>
</section>

<section class="panel side" style="top:848px;height:231px">
  <div class="panel-head">FINANCIAL SUMMARY</div>
  <div class="fin-tabs"><span><i class="radio on"></i>Tax Year</span><span><i class="radio"></i>Current Tax</span></div>
  <div class="stat" style="border-top:none">Paid Invoices<b>£53,769</b></div>
  <div class="stat">Unpaid Invoices<b>£3,188</b></div>
  <div class="stat total">Total Earned<b>£56,957</b></div>
  <div class="stat">Pension Claimed<b>£5,238</b></div>
  <div class="stat">Expenses<b>£2,413</b></div>
</section>

<footer class="footer">
  <span>COPYRIGHT © 2013 TENDRIL HARBOR LTD. ALL RIGHTS RESERVED. REGISTERED IN ENGLAND NO. 08831927</span>
  <span class="links"><span>TERM OF SERVICE</span><span>PRIVACY POLICY</span><span>REFUND POLICY</span></span>
</footer>
</body>
</html>
```